Social Media Graphics - ALL TEXT RK

We are looking for a series of social media graphics for Instagram (standard size 1:1 (1080x1080px) that are ALL TEXT. We want the following quotes below on each graphic; one quote per graphic. AND, In very small letters at the bottom of each graphic, add @RKMarlowLive

The look and feel of these graphics should be complimentary to the color palette attached below; but keep them simple. But the design is up to you; at the end of this document, I provided various samples of all text graphics that I like as examples.

Target Market(s)

women looking to lose weight

Industry/Entity Type

health and wellness

Colors
E54698
E96AAD
F1A4CE
F9D9EA
FCEFF6

Requirements
Must have
• the quotes in the document
Should not have
• no stock photography

```html
<!DOCTYPE html>
<html lang="en">
<head>
<meta charset="utf-8">
<title>RK Social Graphics Series</title>
<link rel="stylesheet" href="https://fonts.googleapis.com/css2?family=Bebas+Neue&family=Alegreya:wght@400&family=Poppins:wght@500&display=swap">
<style>
  :root {
    --pink-strong: #E54698;
    --pink-mid: #E96AAD;
    --pink-soft: #F1A4CE;
    --pink-pale: #F9D9EA;
    --pink-mist: #FCEFF6;
    --ink: #0d0b0c;
    --canvas: #ffffff;
  }
  * { margin: 0; padding: 0; box-sizing: border-box; }
  html, body {
    width: 1200px; height: 2854px; overflow: hidden; background: var(--canvas);
  }
  .sheet { position: relative; width: 1200px; height: 2854px; }
  .post {
    position: absolute; width: 484px; height: 484px;
    background:
      radial-gradient(ellipse 40% 30% at 25% 30%, rgba(233,106,173,0.25), transparent 70%),
      radial-gradient(ellipse 30% 25% at 60% 12%, rgba(233,106,173,0.22), transparent 70%),
      linear-gradient(to bottom right, #F2B6D8 0%, #F4BFDD 49.8%, var(--pink-pale) 50.2%, #F8D3E6 100%);
  }
  .post .frame {
    position: absolute; inset: 26px; border: 2px solid var(--pink-soft);
  }
  .post .message {
    position: absolute; left: 30px; right: 30px; top: 34px; height: 345px;
    display: flex; flex-direction: column; align-items: center; justify-content: center;
    text-align: center; color: var(--ink);
  }
  .headline {
    font-family: "Bebas Neue", "Oswald", sans-serif;
    font-size: 58px; line-height: 1.02; letter-spacing: -0.5px;
  }
  .sub {
    font-family: "Alegreya", Georgia, serif;
    font-size: 31px; line-height: 1.08; text-transform: uppercase;
  }
  .sub.small { font-size: 25px; }
  .handle-bar {
    position: absolute; left: 38px; top: 389px; width: 406px; height: 44px;
    background: linear-gradient(to right, var(--pink-strong), var(--pink-mid) 35%, var(--pink-soft) 70%, var(--pink-pale));
    display: flex; align-items: center; justify-content: center;
    font-family: "Poppins", Arial, sans-serif; font-weight: 500; font-size: 12px; color: #2a1a22;
  }
  .col-left { left: 84px; }
  .col-right { left: 612px; }
  .row-1 { top: 133px; }
  .row-2 { top: 660px; }
  .row-3 { top: 1193px; }
  .row-4 { top: 1731px; }
  .row-5 { top: 2269px; }
</style>
</head>
<body>
<main class="sheet">

  <section class="post col-left row-1">
    <div class="frame"></div>
    <div class="message">
      <p class="headline">Wake up tomorrow<br>with a flatter belly</p>
      <p class="sub">Yes, this overnight<br>remedy works<br>like magic!</p>
    </div>
    <div class="handle-bar">@RKMarlowLive</div>
  </section>

  <section class="post col-right row-1">
    <div class="frame"></div>
    <div class="message">
      <p class="sub small">Struggling with<br>bloating and belly fat?</p>
      <p class="headline" style="font-size:48px;line-height:1.15">Try this natural solution<br>tonight, and wake up<br>feeling lighter!</p>
    </div>
    <div class="handle-bar">@RKMarlowLive</div>
  </section>

  <section class="post col-left row-2">
    <div class="frame"></div>
    <div class="message">
      <p class="headline" style="font-size:66px;line-height:1.05">One supplement,<br>one night;</p>
      <p class="sub small">Your belly bloat could be<br>gone by morning.<br>Here's how it works!</p>
    </div>
    <div class="handle-bar">@RKMarlowLive</div>
  </section>

  <section class="post col-right row-2">
    <div class="frame"></div>
    <div class="message">
      <p class="headline" style="font-size:66px;line-height:1.02">Finally-a natural<br>solution</p>
      <p class="sub small" style="font-size:27px">That flattens your belly<br>and eases stomach<br>bloat</p>
    </div>
    <div class="handle-bar">@RKMarlowLive</div>
  </section>

  <section class="post col-left row-3">
    <div class="frame"></div>
    <div class="message">
      <p class="headline">Your hormones are<br>out of whack</p>
      <p class="sub small" style="font-size:27px">That's why the weight<br>won't budge! Sis,</p>
    </div>
    <div class="handle-bar">@RKMarlowLive</div>
  </section>

  <section class="post col-right row-3">
    <div class="frame"></div>
    <div class="message">
      <p class="headline" style="font-size:46px;line-height:1.06">Frustrated with belly fat<br>that won't budge?</p>
      <p class="sub small" style="font-size:23px">I've got the solution<br>that finally worked for<br>me-no crazy diets required.</p>
    </div>
    <div class="handle-bar">@RKMarlowLive</div>
  </section>

  <section class="post col-left row-4">
    <div class="frame"></div>
    <div class="message">
      <p class="headline" style="font-size:54px">That stubborn belly<br>fat isn't your fault</p>
      <p class="sub" style="font-size:29px">Here's what<br>no one tells you.</p>
    </div>
    <div class="handle-bar">@RKMarlowLive</div>
  </section>

  <section class="post col-right row-4">
    <div class="frame"></div>
    <div class="message">
      <p class="sub small" style="font-size:28px">You've been lied to</p>
      <p class="headline" style="font-size:66px;line-height:1.05">Just eat less and<br>exercise more'<br>doesn't work in<br>menopause</p>
    </div>
    <div class="handle-bar">@RKMarlowLive</div>
  </section>

  <section class="post col-left row-5">
    <div class="frame"></div>
    <div class="message">
      <p class="sub small" style="font-size:23px">A natural way to<br>boost GLP-1</p>
      <p class="headline" style="font-size:56px;line-height:1.1">No injections,<br>no side effects,<br>just real results.<br>Here's how it works</p>
    </div>
    <div class="handle-bar">@RKMarlowLive</div>
  </section>

  <section class="post col-right row-5">
    <div class="frame"></div>
    <div class="message">
      <p class="headline" style="font-size:62px;line-height:1.05">GLP-1: The magic<br>behind the weight<br>loss drugs.</p>
      <p class="sub small" style="font-size:23px">But here's the secret - you<br>can boost it naturally<br>without a prescription!</p>
    </div>
    <div class="handle-bar">@RKMarlowLive</div>
  </section>

</main>
</body>
</html>
```